Business Card for Luxury Hospitality Industry Career Seeker

Need something Simple, Punctual, and Elegant.

Project goal is to update phone number, layout, and wording

I look forward to working with you to create a business card I can give to managers and employers in the Luxury Hospitality industry. I want to advance a career in this industry handing out cards to managers and directors on my way up.
Updates

Updated graphics preferences in brief - would like my name flanked by small Lion, Compass, & Rope and have the Halworth 5 Star logo on the back Added Saturday, January 14, 2017

Updated Brief:-Some wording has been removed-Card Front should be more simple and tidy now-Card Back word choice & flow is improved Added Sunday, January 15, 2017

Target Market(s)

Luxury Hospitality Industry Employers and Managers

Industry/Entity Type

Hospitality

Contact Information for Business Card

(Card Front)
Corbin T. Pellman (flanked by small Lion, Compass & Rope graphic)
Luxury Hospitality
555-317-8846
ridgefellow@mailvessel.example
netroster.example/in/corbin-pellman-vet-civ
My Experience = Our Success

(Card Back)
Graphic of: Halworth 5 Star logo and maybe QTR 5 Diamond Logo too
8 years military supply, logistics, & administrative experience
2 years intensive recruiting, marketing, and sales expertise
Adept problem solving, planning and management skills
5 Star, 5 Daimond, Luxury Hotels & Hospitality Rooms & Revenue

Requirements
Must have
• Name
• Phone Number
• Email Address
• Net Roster Address
• Slogan (My Experience = Our Success)
• Graphic on back: Halworth 5 Star logo
• Qualification Remarks
• Catchy logo
Nice to have
• Background that makes a viewer think Luxury Hospitality Experience and/or World Experience
• Color combinations I've seen & liked are black & yellow, black & white, and blue & white

```html
<!DOCTYPE html>
<html lang="en">
<head>
<meta charset="utf-8">
<title>Corbin T. Pellman – Business Card</title>
<link rel="stylesheet" href="https://fonts.googleapis.com/css2?family=Cinzel:wght@500&family=Roboto:ital,wght@0,300;0,400;0,500;1,300&display=swap">
<style>
  :root {
    --page-bg: #5b5b5b;
    --card-front: #ffffff;
    --card-back: #02030a;
    --ink: #0b0b0b;
    --accent-yellow: #e2d41a;
    --badge-gold: #a8894f;
    --badge-blue: #1d5fae;
    --emblem-tone: #1a1a1a;
  }
  * { margin: 0; padding: 0; box-sizing: border-box; }
  html, body { width: 1200px; height: 1200px; overflow: hidden; }
  body { background: var(--page-bg); position: relative; font-family: "Roboto", sans-serif; }

  .card {
    position: absolute;
    left: 150px;
    width: 900px;
    height: 511px;
    box-shadow: 0 4px 14px rgba(0,0,0,0.35);
  }
  .card--front { top: 64px; background: var(--card-front); color: var(--ink); }
  .card--back { top: 625px; background: var(--card-back); color: var(--accent-yellow); }

  .line { position: absolute; left: 0; right: 0; text-align: center; white-space: nowrap; }

  .emblem { position: absolute; top: 132px; width: 100px; height: 112px; }
  .emblem--left { left: 84px; }
  .emblem--right { left: 716px; }

  .name {
    top: 152px;
    font-family: "Cinzel", serif;
    font-weight: 500;
    font-size: 46px;
    line-height: 56px;
    letter-spacing: 0;
  }
  .title { top: 207px; font-size: 23px; line-height: 28px; font-weight: 400; }
  .rule { position: absolute; top: 249px; left: 178px; width: 544px; height: 1.5px; background: var(--ink); }
  .phone { top: 306px; font-size: 27px; line-height: 32px; font-weight: 500; }
  .email { top: 337px; font-size: 23px; line-height: 28px; }
  .web { top: 367px; font-size: 23px; line-height: 28px; }
  .slogan { top: 450px; font-size: 26px; line-height: 30px; font-weight: 300; font-style: italic; }

  .qual { font-size: 25px; line-height: 30px; font-weight: 300; }
  .qual--1 { top: 114px; }
  .qual--2 { top: 157px; }
  .qual--3 { top: 201px; }
  .qual--4 { top: 244px; }

  .badge { position: absolute; }
  .badge--rating { left: 285px; top: 340px; width: 110px; height: 110px; border-radius: 50%; background: var(--badge-gold); }
  .badge--award { left: 502px; top: 340px; width: 115px; height: 110px; background: var(--badge-blue); }
</style>
</head>
<body>
  <section class="card card--front">
    <svg class="emblem emblem--left" role="img" aria-label="Small Lion, Compass & Rope emblem" viewBox="0 0 100 112">
      <rect width="100" height="112" rx="10" fill="var(--emblem-tone)"/>
    </svg>
    <svg class="emblem emblem--right" role="img" aria-label="Small Lion, Compass & Rope emblem" viewBox="0 0 100 112">
      <rect width="100" height="112" rx="10" fill="var(--emblem-tone)"/>
    </svg>

    <h1 class="line name">Corbin T. Pellman</h1>
    <p class="line title">Reservations Agent Halworth 5 Star Luxury Hotel</p>
    <div class="rule"></div>

    <p class="line phone">555-317-8846</p>
    <p class="line email">ridgefellow@mailvessel.example</p>
    <p class="line web">netroster.example/in/corbin-pellman-vet-civ</p>

    <p class="line slogan">My Experience = Our Success</p>
  </section>

  <section class="card card--back">
    <p class="line qual qual--1">8 years military supply, logistics, &amp; administrative experience</p>
    <p class="line qual qual--2">2 years intensive recruiting, marketing, and sales expertise</p>
    <p class="line qual qual--3">Adept problem solving, planning and management skills</p>
    <p class="line qual qual--4">5 Star, 5 Daimond, Luxury Hotels &amp; Hospitality Rooms &amp; Revenue</p>

    <div class="badge badge--rating" role="img" aria-label="Halworth 5 Star rating badge"></div>
    <div class="badge badge--award" role="img" aria-label="QTR 5 Diamond award badge"></div>
  </section>
</body>
</html>
```